Stationery for use with Vellmar reports

I would like to get a stationery design that my firm -- Vellmar Partners -- will use as a format for reports that we send our clients. I am specifically looking for a design for use on a piece of paper or letterhead -- not business cards or envelopes.

We are an Africa based US risk intelligence and strategy firm that works with multinational corporations operating in West Africa. Our initial thinking is that we would like a color scheme consistent with our existing logo -- however we are open to other color schemes.

Also, we would like to see at least two separate versions: one with our company name and logo, the other without name and logo.

We also would like font recommendations for the stationary design.

The final design should communicate discreet professionalism and a modern approach, but it should not overshadow the words and information printed on the stationery.

Target Market(s)

Multinational corporations that currently use our products.

Font styles to use
Serif
Sans Serif

Requirements
Must have
• Sense of discreet professionalism that will not overshadow the content we put onto the stationery format.
• We would like to see designs with and without our company name/logo.
• Please suggest fonts that would work with the stationery.
Nice to have
• Ideally colors consistent with out existing logo, though we are open to and even encourage other ideas.
Should not have
• No need for business cards or envelopes.

```html
<!DOCTYPE html>
<html lang="en">
<head>
<meta charset="utf-8">
<title>Vellmar Partners — Letterhead</title>
<link rel="stylesheet" href="https://fonts.googleapis.com/css2?family=Nunito+Sans:wght@400;800&display=swap">
<style>
  :root {
    --ink: #1a1a1a;
    --navy: #263e4a;
    --gold: #e3a94f;
    --sky: #a9d5ef;
    --paper: #ffffff;
  }
  * { margin: 0; padding: 0; box-sizing: border-box; }
  html, body { width: 927px; height: 1200px; overflow: hidden; background: var(--paper); }
  body { font-family: "Nunito Sans", "Avenir Next", Arial, sans-serif; color: var(--ink); }
  .letterhead { position: relative; width: 927px; height: 1200px; }

  .brand {
    position: absolute; left: 83px; top: 120px;
    display: flex; align-items: center; gap: 12px;
  }
  .brand-mark { width: 18px; height: 18px; background: var(--gold); }
  .brand-name {
    font-weight: 800; font-size: 30px; line-height: 1.05; color: var(--navy);
  }

  .contact { position: absolute; left: 604px; top: 56px; }
  .contact-row { position: absolute; left: 0; display: flex; }
  .contact-icon {
    width: 43px; height: 43px; border: 3px solid var(--gold);
    display: flex; align-items: center; justify-content: center;
  }
  .contact-icon svg { width: 32px; height: 32px; }
  .contact-text {
    position: absolute; left: 53px; white-space: nowrap;
    font-size: 16.5px; line-height: 20px; color: var(--ink); letter-spacing: 0.3px;
  }
  .row-email { top: 0; }
  .row-email .contact-text { top: 2px; }
  .row-phone { top: 47px; }
  .row-phone .contact-text { top: 2px; left: 50px; }
  .row-address { top: 94px; }
  .row-address .contact-text { top: -3px; }

  .letter { position: absolute; left: 83px; top: 256px; width: 760px; font-size: 20px; line-height: 24.7px; }
  .letter-date { margin-bottom: 25px; }
  .letter-recipient { margin-bottom: 25px; }
  .letter-body p { text-align: justify; margin-bottom: 24.7px; }
  .letter-closing { margin-top: 0; }
  .letter-signature { margin-top: 74px; }
</style>
</head>
<body>
<main class="letterhead">
  <div class="brand">
    <span class="brand-mark"></span>
    <span class="brand-name">Vellmar<br>Partners</span>
  </div>

  <aside class="contact">
    <div class="contact-row row-email">
      <span class="contact-icon">
        <svg viewBox="0 0 32 32" aria-hidden="true">
          <path d="M3 12 L16 5 L29 12 L29 26 L3 26 Z" fill="var(--sky)"/>
          <path d="M3 12 L16 19 L29 12" fill="none" stroke="#fff" stroke-width="2"/>
        </svg>
      </span>
      <span class="contact-text">info@vellmarpartners.com</span>
    </div>
    <div class="contact-row row-phone">
      <span class="contact-icon">
        <svg viewBox="0 0 32 32" aria-hidden="true">
          <path d="M6 3 C3 5 2 10 6 17 C10 24 16 29 22 30 C26 30 29 27 28 25 L24 20 C23 19 21 19 20 21 C18 22 16 20 13 16 C10 12 10 10 12 9 C13 8 13 6 12 5 L9 2 C8 1 7 2 6 3 Z" fill="var(--sky)"/>
        </svg>
      </span>
      <span class="contact-text">+1 (555) 014 2290</span>
    </div>
    <div class="contact-row row-address">
      <span class="contact-icon">
        <svg viewBox="0 0 32 32" aria-hidden="true">
          <rect x="3" y="4" width="14" height="26" fill="var(--sky)"/>
          <rect x="19" y="13" width="11" height="17" fill="var(--sky)"/>
          <g fill="#fff">
            <rect x="6" y="8" width="3" height="3"/><rect x="11" y="8" width="3" height="3"/>
            <rect x="6" y="14" width="3" height="3"/><rect x="11" y="14" width="3" height="3"/>
            <rect x="6" y="20" width="3" height="3"/><rect x="11" y="20" width="3" height="3"/>
            <rect x="22" y="22" width="5" height="8"/>
          </g>
        </svg>
      </span>
      <span class="contact-text">2218 Halden Ridge Road #4410<br>Ashford, Virginia 22190<br>USA</span>
    </div>
  </aside>

  <article class="letter">
    <p class="letter-date">February 27th, 2020</p>
    <p class="letter-recipient">2218 Halden Ridge Road #4410<br>Ashford, Virginia 22190<br>USA</p>
    <div class="letter-body">
      <p>Lorem ipsum dolor sit amet, consectetur adipisicing elit, sed do eiusmod tempor incididunt ut labore et dolore magna aliqua. Ut enim ad minim veniam, quis nostrud exercitation ullamco laboris nisi ut aliquip ex ea commodo consequat. Duis aute irure dolor in reprehenderit in voluptate velit esse cillum dolore eu fugiat nulla pariatur. Excepteur sint occaecat cupidatat non proident, sunt in culpa qui officia deserunt mollit anim id est laborum. Sed ut perspiciatis unde omnis iste natus error sit voluptatem accusantium doloremque laudantium, totam rem aperiam, eaque ipsa quae ab illo inventore veritatis et quasi architecto beatae vitae dicta sunt explicabo. Nemo enim ipsam voluptatem quia voluptas sit aspernatur aut odit aut fugit, sed quia consequuntur magni dolores eos qui ratione voluptatem sequi nesciunt.</p>
      <p>Lorem ipsum dolor sit amet, consectetur adipisicing elit, sed do eiusmod tempor incididunt ut labore et dolore magna aliqua. Ut enim ad minim veniam, quis nostrud exercitation ullamco laboris nisi ut aliquip ex ea commodo consequat. Duis aute irure dolor in reprehenderit in voluptate velit esse cillum dolore eu fugiat nulla pariatur. Excepteur sint occaecat cupidatat non proident, sunt in culpa qui officia deserunt mollit anim id est laborum. Sed ut perspiciatis unde omnis iste natus error sit voluptatem accusantium doloremque laudantium, totam rem aperiam, eaque ipsa quae ab illo inventore veritatis et quasi architecto beatae vitae dicta sunt explicabo. Nemo enim ipsam voluptatem quia voluptas sit aspernatur aut odit aut fugit, sed quia consequuntur magni dolores eos qui ratione voluptatem sequi nesciunt.</p>
    </div>
    <p class="letter-closing">Kind regards,</p>
    <p class="letter-signature">Jordan Reese</p>
  </article>
</main>
</body>
</html>
```